Redesign This Psychology Website

We would like a slight redesign of this successful psychology (relationship counselling) website:

www.TheWillowNook.com.au

We are updating the website, and we'd like a slight refresh of the design and style.

Please keep to very similar colours, and use the same logo. We're looking for around 10 page templates, however the main one is the home page.

Keep in mind, this website already converts quite well, so we want a new, fresh design in keeping with this one. Please don't bother designing something too extremely different.

thanks :)

Target Market(s)

couples who are looking for relationship counselling. Men and women, 25 - 70, across Australia

Industry/Entity Type

Psychology

Number of Pages Required

5+ page

Font styles to use
Sans Serif

Colors
87cfc6
b7a5cd
ec1f27
ffffff
cee9f5

Requirements
Must have
• a similar look to the current design, just looking for a slight refresh.
• Search bar
• Areas for lots of photos
• same logo
• lots of content areas
Nice to have
• great content areas, where we can display a lot of content and our areas.
Should not have
• no colors like orange, etc.
• should not have a totally different feel.

```html
<!DOCTYPE html>
<html lang="en">
<head>
<meta charset="utf-8">
<title>About Us – The Willow Nook</title>
<link rel="stylesheet" href="https://fonts.googleapis.com/css2?family=Lato:wght@400;700&family=Mulish:wght@400;600;700&display=swap">
<style>
:root{
  --teal:#87cfc6;
  --teal-dark:#5fb8ad;
  --lavender:#b7a5cd;
  --red:#ec1f27;
  --sky:#cee9f5;
  --white:#ffffff;
  --ink:#2d2d2d;
  --body:#6d6d6d;
  --muted:#9a9a9a;
  --rule:#e3e3e3;
  --bar:#f1f1f1;
  --footer:#efefef;
}
*{box-sizing:border-box;margin:0;padding:0}
html,body{width:1200px;height:3974px;overflow:hidden}
body{position:relative;background:var(--white);font-family:"Lato",sans-serif;color:var(--body)}
a{color:inherit;text-decoration:none}
.abs{position:absolute}

.utility-bar{left:0;top:0;width:1200px;height:40px;background:var(--bar);border-bottom:1px solid var(--rule)}
.utility-bar .associate{position:absolute;left:127px;top:12px;font-size:13px;color:#777}
.utility-links{position:absolute;right:127px;top:0;display:flex;height:40px;align-items:center}
.utility-links a{font-size:13px;color:#888;padding:0 10px;border-left:1px solid #d6d6d6}
.utility-links a:first-child{border-left:none}

.site-header{left:0;top:40px;width:1200px;height:114px}
.brand{position:absolute;left:127px;top:26px;display:flex;align-items:center;gap:12px}
.brand-dot{width:44px;height:44px;border-radius:50%;background:var(--teal)}
.brand-name{font-family:"Mulish",sans-serif;font-weight:700;font-size:30px;color:var(--teal-dark);line-height:1}
.brand-tag{position:absolute;left:183px;top:70px;font-size:13px;color:var(--muted)}
.search{position:absolute;left:458px;top:44px;width:355px;height:38px;border:1px solid #d8d8d8;border-radius:3px;display:flex;align-items:center;padding-left:12px;gap:8px;font-size:13px;color:#aaa}
.call{position:absolute;right:127px;top:30px;text-align:right}
.call small{display:block;font-size:15px;color:var(--teal-dark)}
.call strong{display:flex;align-items:center;gap:8px;font-size:25px;font-weight:700;color:var(--red)}

.main-nav{left:0;top:154px;width:1200px;height:72px;background:linear-gradient(var(--teal),#7ac6bc);display:flex;justify-content:center}
.main-nav ul{list-style:none;display:flex;width:946px}
.main-nav li{display:flex;align-items:center;padding:0 14px;border-left:1px solid rgba(255,255,255,.55);color:var(--white);font-family:"Mulish",sans-serif;font-weight:600;font-size:16px;line-height:1.2;text-transform:uppercase}
.main-nav li:first-child{border-left:none;padding-left:0}

.hero{left:0;top:226px;width:1200px;height:330px;background:linear-gradient(100deg,#6f5a55 0%,#a88e86 35%,#d9c6bd 60%,#8d7570 100%)}
.hero h1{position:absolute;left:127px;top:168px;font-family:"Mulish",sans-serif;font-weight:600;font-size:44px;color:var(--white);letter-spacing:.5px}

.intro{left:127px;top:605px;width:615px}
.intro h2{font-family:"Mulish",sans-serif;font-weight:400;font-size:30px;line-height:1.2;color:var(--ink);margin-bottom:14px}
.intro p{font-size:13.4px;line-height:19px;margin-bottom:10px}

.section-title{left:127px;top:1075px;font-family:"Mulish",sans-serif;font-weight:400;font-size:28px;color:var(--red)}

.psych{left:127px;width:615px;display:flex;gap:34px}
.psych-photo{flex:none;width:120px;height:120px;border-radius:50%;margin-top:4px}
.psych-body{width:461px}
.psych-name{font-family:"Mulish",sans-serif;font-weight:700;font-size:20px;color:var(--teal-dark);margin-bottom:3px}
.psych-role,.psych-quals{font-size:12.5px;line-height:17px;color:#555}
.psych-cert{font-size:12.5px;line-height:20px;color:var(--teal-dark);margin-top:2px}
.psych-bio{font-size:12px;line-height:16.5px;color:var(--muted);margin-top:2px}
.psych-cta{display:flex;align-items:center;gap:14px;margin-top:12px}
.btn-outline{border:1px solid var(--lavender);color:var(--lavender);font-size:12px;font-weight:700;letter-spacing:.5px;padding:7px 14px}
.psych-cta span{font-size:12px;color:#444;font-weight:700}

.finder{left:768px;top:599px;width:305px;height:334px;background:var(--lavender);padding:20px 22px}
.finder h3{font-family:"Mulish",sans-serif;font-weight:700;font-size:22px;color:var(--white);text-align:center;line-height:1.25;margin-bottom:14px}
.finder label{display:block;font-size:13px;color:var(--white);margin:8px 0 4px}
.finder .field{height:30px;background:var(--white);font-size:12px;color:#999;padding:7px 10px}
.finder .btn-search{margin-top:14px;height:36px;background:var(--red);color:var(--white);font-weight:700;font-size:15px;text-align:center;line-height:36px}

.post{left:768px;width:305px;height:116px;display:flex;gap:14px;align-items:center}
.post-thumb{flex:none;width:165px;height:110px}
.post h4{font-size:14.5px;font-weight:400;color:var(--ink);line-height:19px}
.post a{display:block;font-size:11.5px;color:var(--teal-dark);margin-top:4px}

.categories{left:768px;top:2167px;width:305px;height:867px;border:1px solid var(--rule)}
.categories h3{background:var(--lavender);color:var(--white);font-family:"Mulish",sans-serif;font-weight:700;font-size:20px;height:60px;line-height:60px;padding-left:22px}
.categories ul{list-style:none;padding:14px 22px}
.categories li{display:flex;align-items:center;gap:12px;font-size:13px;color:#555;height:31px}
.categories li::before{content:"";width:6px;height:6px;border-top:2px solid var(--teal-dark);border-right:2px solid var(--teal-dark);transform:rotate(45deg)}

.site-footer{left:0;top:3610px;width:1200px;height:286px;background:var(--footer)}
.footer-brand{position:absolute;left:142px;top:70px;display:flex;align-items:center;gap:12px}
.footer-tag{position:absolute;left:198px;top:116px;font-size:12px;color:var(--muted)}
.footer-col{position:absolute;top:60px}
.footer-col h5{font-family:"Mulish",sans-serif;font-weight:700;font-size:16px;color:var(--teal-dark);margin-bottom:10px}
.footer-col li{list-style:none;font-size:13px;color:#666;line-height:23px}
.social{display:flex;gap:10px;margin-top:14px}
.social span{width:30px;height:30px;border-radius:50%;background:var(--teal-dark)}
.social span:nth-child(2){background:#6d8cbf}
.social span:nth-child(3){background:#5a8fbd}
.social span:nth-child(4){background:#d9726a}
.copyright{left:0;top:3896px;width:1200px;height:78px;background:#e4e4e4;text-align:center;line-height:78px;font-size:12px;color:#888}
</style>
</head>
<body>

<div class="abs utility-bar">
  <a class="associate" href="#">Join Our Associate Program →</a>
  <nav class="utility-links"><a href="#">Home</a><a href="#">Cart</a><a href="#">Blog</a><a href="#">Resources</a><a href="#">Contact Us</a></nav>
</div>

<header class="abs site-header">
  <div class="brand"><span class="brand-dot"></span><span class="brand-name">The Willow Nook</span></div>
  <div class="brand-tag">helping you create loving relationships</div>
  <div class="search">
    <svg width="14" height="14" viewBox="0 0 14 14"><circle cx="6" cy="6" r="4.5" fill="none" stroke="#aaa" stroke-width="1.5"/><line x1="9.3" y1="9.3" x2="13" y2="13" stroke="#aaa" stroke-width="1.5"/></svg>
    Search here
  </div>
  <div class="call">
    <small>Call Us Now</small>
    <strong><svg width="22" height="22" viewBox="0 0 24 24"><path d="M6.6 10.8a15 15 0 0 0 6.6 6.6l2.2-2.2a1 1 0 0 1 1-.25 11.4 11.4 0 0 0 3.6.57 1 1 0 0 1 1 1V20a1 1 0 0 1-1 1A17 17 0 0 1 3 4a1 1 0 0 1 1-1h3.5a1 1 0 0 1 1 1c0 1.25.2 2.45.57 3.57a1 1 0 0 1-.25 1z" fill="none" stroke="#ec1f27" stroke-width="1.8"/></svg>1300 555 014</strong>
  </div>
</header>

<nav class="abs main-nav">
  <ul>
    <li>Counselling<br>Types</li>
    <li>Relationship Counselling<br>Locations</li>
    <li>Sex Therapy<br>Locations</li>
    <li>About Us</li>
    <li>Quizzes</li>
    <li>FAQ's</li>
    <li>Contact</li>
  </ul>
</nav>

<section class="abs hero" role="img" aria-label="Photo of a couple lying together, smiling and relaxed">
  <h1>ABOUT US</h1>
</section>

<section class="abs intro">
  <h2>The Willow Nook is a company passionate about creating healthy loving relationships, of all kinds.</h2>
  <p>Our mission is to be the most highly regarded relationship help service in Australia, by delivering a comprehensive range of the highest quality relationship and marriage counselling and advice, and books and products to educate and enhance client's relationships. To have every client who comes through our doors leave feeling listened to, understood, and educated on how to build a better relationship with their partner, while at the same time bringing out the best in themselves.</p>
  <p>We have been in operation for 16 years in Australia.</p>
  <p>Our counsellors are all Psychologists, and in addition, we have our own in-house relationship counselling training program, and ongoing professional development program, and are constantly seeking best practice methodologies.</p>
  <p>With our specialized experience in relationship and marriage counselling, together with our caring, compassionate and unbiased approach, you are in safe and experienced hands.</p>
</section>

<h2 class="abs section-title">Our Psychologists</h2>

<article class="abs psych" style="top:1134px">
  <div class="psych-photo" role="img" aria-label="Portrait photo of Leanne" style="background:radial-gradient(circle at 50% 40%,#f1cfa8,#d9a05c 70%,#c98a45)"></div>
  <div class="psych-body">
    <h3 class="psych-name">Leanne</h3>
    <p class="psych-role">Registered Psychologist Sydney</p>
    <p class="psych-quals">BA (Psych), Grad Dip (Psych), Grad Dip (Rel Couns &amp; Fam Therapy) MPPA</p>
    <p class="psych-cert">Willow Nook Certified</p>
    <p class="psych-bio">Leanne is a registered psychologist and qualified relationship and family counsellor since 2006. She has worked for non-for-profit organisations and the community sector for over twenty years. Leanne sees individuals, couples and families, and is also an approved provider of insurer-funded care.</p>
    <div class="psych-cta"><a class="btn-outline" href="#">READ MORE</a><span>Or to book an appointment, please call 1300 555 014</span></div>
  </div>
</article>

<article class="abs psych" style="top:1407px">
  <div class="psych-photo" role="img" aria-label="Portrait photo of Miranda" style="background:radial-gradient(circle at 50% 40%,#c99a83,#4a3530 70%,#2e2220)"></div>
  <div class="psych-body">
    <h3 class="psych-name">Miranda</h3>
    <p class="psych-role">Registered Psychologist Sydney</p>
    <p class="psych-quals">BA (Psych), Grad Dip Sc (Psych), Grad Dip (App Psych), MA (Coaching Psychology)</p>
    <p class="psych-cert">Willow Nook Certified</p>
    <p class="psych-bio">Miranda specialises in individual and relationship counselling in Sydney and has worked as a psychologist for over 12 years in a variety of public and private settings. She has previously worked as a school counsellor with children, teenagers and their families, and understands the busy lifestyles many families lead in today's day and age. For these reasons she facilitates online and phone sessions if face-to-face sessions are not possible.</p>
    <div class="psych-cta"><a class="btn-outline" href="#">READ MORE</a><span>Or to book an appointment, please call 1300 555 014</span></div>
  </div>
</article>

<article class="abs psych" style="top:1736px">
  <div class="psych-photo" role="img" aria-label="Portrait photo of Rosalind" style="background:radial-gradient(circle at 50% 40%,#e6bfa0,#8a5a3c 70%,#5c3a28)"></div>
  <div class="psych-body">
    <h3 class="psych-name">Rosalind</h3>
    <p class="psych-role">Registered Psychologist Sydney</p>
    <p class="psych-quals">BA (Psych), Grad Dip (Psych), Grad Dip (Rel Couns &amp; Fam Therapy) MPPA</p>
    <p class="psych-cert">Willow Nook Certified</p>
    <p class="psych-bio">Rosalind is a registered psychologist and qualified relationship and family counsellor since 2006. She has worked for non-for-profit organisations and the community sector for over twenty years. Rosalind sees individuals, couples and families, and is also an approved provider of insurer-funded care.</p>
    <div class="psych-cta"><a class="btn-outline" href="#">READ MORE</a><span>Or to book an appointment, please call 1300 555 014</span></div>
  </div>
</article>

<article class="abs psych" style="top:2022px">
  <div class="psych-photo" role="img" aria-label="Portrait photo of Bernadette" style="background:radial-gradient(circle at 50% 40%,#f0d3c0,#b9b4b0 70%,#8d8a88)"></div>
  <div class="psych-body">
    <h3 class="psych-name">Bernadette</h3>
    <p class="psych-role">Registered Psychologist Melbourne</p>
    <p class="psych-quals">B.Psych (Hons 1st), B.App.Sci. (Health Sci: Hons 1st), Assoc MPPA, Member MRCPA,</p>
    <p class="psych-cert">Willow Nook Certified</p>
    <p class="psych-bio">Bernadette is passionate about couples counselling. Her sincere and genuine desire to assist individuals and couples in creating stronger, healthier and more satisfying relationships has been her guiding motivation for almost two decades of working in the field of relationship psychology. Described by both clients and colleagues alike as warm, open, personable and compassionate, her relaxed style provides a comfortable, yet safe, environment within which to explore your relationship issues.</p>
    <div class="psych-cta"><a class="btn-outline" href="#">READ MORE</a><span>Or to book an appointment, please call 1300 555 014</span></div>
  </div>
</article>

<article class="abs psych" style="top:2348px">
  <div class="psych-photo" role="img" aria-label="Portrait photo of Sienna" style="background:radial-gradient(circle at 50% 40%,#d9a98c,#5a3a2c 70%,#3a251d)"></div>
  <div class="psych-body">
    <h3 class="psych-name">Sienna</h3>
    <p class="psych-role">Diploma in Counselling (CIC)</p>
    <p class="psych-cert">Willow Nook Certified</p>
    <p class="psych-bio">Sienna provides marriage counselling in Sydney and has a Diploma of Counselling from the Coastal Institute of Counselling along with being trained through Willow Nook in the development of complex counselling skills. She is a member of the Southern Counsellors Guild and participates in reflective individual and peer clinical supervision on a regular basis.</p>
    <div class="psych-cta"><a class="btn-outline" href="#">READ MORE</a><span>Or to book an appointment, please call 1300 555 014</span></div>
  </div>
</article>

<article class="abs psych" style="top:2637px">
  <div class="psych-photo" role="img" aria-label="Portrait photo of Tamsin" style="background:radial-gradient(circle at 50% 40%,#e2b49a,#8c3f34 70%,#5e2a22)"></div>
  <div class="psych-body">
    <h3 class="psych-name">Tamsin</h3>
    <p class="psych-role">Registered Psychologist Brisbane</p>
    <p class="psych-quals">B Soc Work; B Ed (Hons); B Soc Sci (Psych); Grad Dip Psych; Grad Dip Couns; M Couns</p>
    <p class="psych-cert">Willow Nook Certified</p>
    <p class="psych-bio">Tamsin is passionate about individual and relationship counselling and believes it is an honour and privilege to be allowed to hear somebody's life story. Her experience has involved working with families, couples and individuals dealing with challenging life events such as terminal illness and their bereaved families, partners and friends, and with women, young people and children who have been hurt. Tamsin has an employment history.</p>
    <div class="psych-cta"><a class="btn-outline" href="#">READ MORE</a><span>Or to book an appointment, please call 1300 555 014</span></div>
  </div>
</article>

<article class="abs psych" style="top:2960px">
  <div class="psych-photo" role="img" aria-label="Portrait photo of Noelle" style="background:radial-gradient(circle at 50% 40%,#eccab0,#7a5a44 70%,#4d3829)"></div>
  <div class="psych-body">
    <h3 class="psych-name">Noelle</h3>
    <p class="psych-role">Registered Counsellor</p>
    <p class="psych-quals">B Psych (Hons); Grad Dip Rel Couns; MSCG</p>
    <p class="psych-cert">Willow Nook Certified</p>
    <p class="psych-bio">Noelle provides marriage counselling in Sydney, and has an Honours Degree in Psychology from Harbourside University and a Graduate Diploma of Relationship Counselling from the Lakeview Family Studies College. Noelle is also Willow Nook certified and a registered member of the Southern Counsellors Guild. She engages in regular self-reflection and participates in peer and clinical supervision.</p>
    <div class="psych-cta"><a class="btn-outline" href="#">READ MORE</a><span>Or to book an appointment, please call 1300 555 014</span></div>
  </div>
</article>

<article class="abs psych" style="top:3273px">
  <div class="psych-photo" role="img" aria-label="Portrait photo of Paloma" style="background:radial-gradient(circle at 50% 40%,#f4dcc8,#c9a58a 70%,#a88468)"></div>
  <div class="psych-body">
    <h3 class="psych-name">Paloma</h3>
    <p class="psych-role">Registered Psychologist Sydney</p>
    <p class="psych-quals">B Psych (Hons); Grad Dip Int Comm; PhD; MPPA</p>
    <p class="psych-cert">Willow Nook Certified</p>
    <p class="psych-bio">Dr Paloma is a psychologist in Sydney registered with the national registration board and a full member of the Psychology Practitioners Alliance. She specialises in couples counselling and marital preparation. In addition to her Honours Degree in Psychology, she holds a PhD and a Postgraduate Diploma in Intercultural Communication. She has worked as a psychologist in private, academic and corporate settings.</p>
    <div class="psych-cta"><a class="btn-outline" href="#">READ MORE</a><span>Or to book an appointment, please call 1300 555 014</span></div>
  </div>
</article>

<aside class="abs finder">
  <h3>Find Our Psychologist<br>Near You</h3>
  <label>Type of Counselling</label>
  <div class="field">Select</div>
  <label>Location</label>
  <div class="field"></div>
  <label>Postcode</label>
  <div class="field"></div>
  <div class="btn-search">SEARCH</div>
</aside>

<div class="abs post" style="top:989px"><div class="post-thumb" role="img" aria-label="Photo of two hands holding" style="background:linear-gradient(135deg,#c7a48f,#8f6e60)"></div><div><h4>What can I do if I'm living with a Narcissist?</h4><a href="#">Read More</a></div></div>
<div class="abs post" style="top:1117px"><div class="post-thumb" role="img" aria-label="Photo of a worried woman" style="background:linear-gradient(135deg,#5b5150,#a8948c)"></div><div><h4>Are You Living With a Steamroller?</h4><a href="#">Read More</a></div></div>
<div class="abs post" style="top:1245px"><div class="post-thumb" role="img" aria-label="Photo of a couple arguing" style="background:linear-gradient(135deg,#7a6a62,#c9b6a8)"></div><div><h4>Did Your Relationship Start on Rocky Ground?</h4><a href="#">Read More</a></div></div>
<div class="abs post" style="top:1391px"><div class="post-thumb" role="img" aria-label="Photo of a sad woman sitting" style="background:linear-gradient(135deg,#d8c2b4,#9e8577)"></div><div><h4>Why am I with a Narcissist?</h4><a href="#">Read More</a></div></div>
<div class="abs post" style="top:1519px"><div class="post-thumb" role="img" aria-label="Photo of a couple sitting apart" style="background:linear-gradient(135deg,#b9c4c9,#6e7c84)"></div><div><h4>Letter for a Partner Doubtful About Relationship Counselling</h4><a href="#">Read More</a></div></div>
<div class="abs post" style="top:1647px"><div class="post-thumb" role="img" aria-label="Photo of a couple holding hands outdoors" style="background:linear-gradient(135deg,#d9b59a,#a7745a)"></div><div><h4>What Are You Like In a Relationship?</h4><a href="#">Read More</a></div></div>
<div class="abs post" style="top:1775px"><div class="post-thumb" role="img" aria-label="Photo of a man and woman in conflict" style="background:linear-gradient(135deg,#3c3533,#8a7b74)"></div><div><h4>How Do I Know If I'm With a Narcissist?</h4><a href="#">Read More</a></div></div>
<div class="abs post" style="top:1903px"><div class="post-thumb" role="img" aria-label="Photo of a couple looking away" style="background:linear-gradient(135deg,#e2d2c4,#a99282)"></div><div><h4>Do You Wonder Why You and Your Partner Are Together?</h4><a href="#">Read More</a></div></div>
<div class="abs post" style="top:2031px"><div class="post-thumb" role="img" aria-label="Photo of a thoughtful woman" style="background:linear-gradient(135deg,#8d6f73,#cfb3b0)"></div><div><h4>Is Your Pursuit of Success Sabotaging Your Relationships That Matter Most?</h4><a href="#">Read More</a></div></div>

<aside class="abs categories">
  <h3>Blogs Categories</h3>
  <ul>
    <li>Affairs</li><li>Assertiveness</li><li>Attachment</li><li>Break up</li><li>Communication</li>
    <li>Compatibility</li><li>Controlling</li><li>Couples counselling</li><li>Empathy</li><li>Enneagram</li>
    <li>Financial stress</li><li>Individual counselling for relationships</li><li>Infertility</li><li>Intimacy</li><li>Marriage counselling</li>
    <li>Narcissism</li><li>Personal growth</li><li>Personality</li><li>psychological wellbeing</li><li>Psychologist Interviews</li>
    <li>Relationship counselling</li><li>Relationship happiness</li><li>Relationship problems</li><li>Singles</li><li>Uncategorised</li>
  </ul>
</aside>

<footer class="abs site-footer">
  <div class="footer-brand"><span class="brand-dot"></span><span class="brand-name">The Willow Nook</span></div>
  <div class="footer-tag">helping you create loving relationships</div>
  <div class="footer-col" style="left:462px">
    <h5>QUICK LINKS</h5>
    <ul><li>Home</li><li>About Us</li><li>Our Blogs</li><li>Shop Cart</li><li>Contact Us</li></ul>
  </div>
  <div class="footer-col" style="left:630px">
    <h5>RESOURCES</h5>
    <ul><li>Counselling Type</li><li>Sex Therapy</li><li>Quizzes</li><li>FAQ</li><li>Relationship Counselling</li></ul>
  </div>
  <div class="footer-col" style="left:834px">
    <h5>CONTACT US</h5>
    <ul><li>27 Fernleigh Parade Suite 4</li><li>1300 555 014</li><li>Email: info@willownook.com.au</li></ul>
    <div class="social"><span></span><span></span><span></span><span></span></div>
  </div>
</footer>
<div class="abs copyright">© 2017 Company Name. All right reserved</div>

</body>
</html>
```